Tandrel needs stationery design

We need desings for presentation cards and letter head for our company. It would be better that the letterhead uses our logo with white background and the presentation card the logo with the black background for the back of the card and the text (name, phone

Colors
0455a3
ec1f27
000000

Requirements
Must have
• Use company logo and colors

```html
<!DOCTYPE html>
<html lang="en">
<head>
<meta charset="utf-8">
<title>Tandrel – Business Card</title>
<link rel="stylesheet" href="https://fonts.googleapis.com/css2?family=Hind:wght@400;500&display=swap">
<style>
  :root {
    --brand-blue: #0455a3;
    --brand-red: #ec1f27;
    --brand-black: #000000;
    --text-light: #ffffff;
    --page-bg: #ffffff;
  }
  * { margin: 0; padding: 0; box-sizing: border-box; }
  html, body {
    width: 1200px;
    height: 420px;
    overflow: hidden;
    background: var(--page-bg);
    font-family: "Hind", "Segoe UI", sans-serif;
  }
  .sheet {
    position: relative;
    width: 1200px;
    height: 420px;
  }
  .card {
    position: absolute;
    top: 58px;
    width: 536px;
    height: 309px;
    overflow: hidden;
    background: var(--brand-black);
  }
  .card--front { left: 48px; }
  .card--back { left: 616px; }
  .card__art {
    position: absolute;
    inset: 0;
    width: 100%;
    height: 100%;
  }
  .wordmark {
    position: absolute;
    color: var(--text-light);
    font-weight: 500;
    text-transform: uppercase;
    line-height: 1;
    white-space: nowrap;
  }
  .card--front .wordmark {
    left: 268px;
    top: 156px;
    transform: translate(-50%, -50%);
    font-size: 44px;
    letter-spacing: 4px;
  }
  .card--back .wordmark {
    left: 64px;
    top: 157px;
    transform: translateY(-50%);
    font-size: 21px;
    letter-spacing: 2px;
  }
  .contact-list {
    position: absolute;
    left: 254px;
    top: 87px;
    list-style: none;
  }
  .contact-list__item {
    display: flex;
    align-items: center;
    height: 24px;
    margin-bottom: 13px;
    color: var(--text-light);
    font-size: 12.5px;
    font-weight: 400;
    white-space: nowrap;
  }
  .contact-list__icon {
    width: 14px;
    height: 14px;
    margin-right: 17px;
    flex: none;
    fill: var(--brand-red);
  }
</style>
</head>
<body>
<main class="sheet">

  <section class="card card--front" aria-label="Card front">
    <svg class="card__art" viewBox="0 0 536 309" aria-hidden="true">
      <defs>
        <linearGradient id="front-field" x1="0" y1="0" x2="1" y2="1">
          <stop offset="0" stop-color="#101a2e"/>
          <stop offset="0.5" stop-color="#0a1326"/>
          <stop offset="1" stop-color="#0d1a33"/>
        </linearGradient>
        <radialGradient id="front-texture-left" cx="0" cy="0.5" r="0.9">
          <stop offset="0" stop-color="#1a2c4d" stop-opacity="0.8"/>
          <stop offset="1" stop-color="#1a2c4d" stop-opacity="0"/>
        </radialGradient>
        <radialGradient id="front-texture-right" cx="1" cy="0.5" r="0.9">
          <stop offset="0" stop-color="#1b3158" stop-opacity="0.8"/>
          <stop offset="1" stop-color="#1b3158" stop-opacity="0"/>
        </radialGradient>
        <linearGradient id="front-rim" x1="0" y1="0" x2="1" y2="1">
          <stop offset="0" stop-color="#0455a3" stop-opacity="0.2"/>
          <stop offset="0.45" stop-color="#1a6fd0"/>
          <stop offset="1" stop-color="#0455a3"/>
        </linearGradient>
      </defs>
      <rect width="536" height="309" fill="url(#front-field)"/>
      <rect width="200" height="309" fill="url(#front-texture-left)"/>
      <rect x="336" width="200" height="309" fill="url(#front-texture-right)"/>
      <ellipse cx="262" cy="152" rx="206" ry="170" fill="url(#front-rim)" opacity="0.9"/>
      <ellipse cx="270" cy="146" rx="202" ry="168" fill="var(--brand-black)"/>
    </svg>
    <div class="wordmark">Tandrel</div>
  </section>

  <section class="card card--back" aria-label="Card back">
    <svg class="card__art" viewBox="0 0 536 309" aria-hidden="true">
      <defs>
        <linearGradient id="back-texture" x1="1" y1="0" x2="0" y2="0">
          <stop offset="0" stop-color="#0d3c7a" stop-opacity="0.9"/>
          <stop offset="1" stop-color="#0d3c7a" stop-opacity="0"/>
        </linearGradient>
        <linearGradient id="back-corner" x1="0" y1="0" x2="0" y2="1">
          <stop offset="0.4" stop-color="#0b1f3d" stop-opacity="0"/>
          <stop offset="1" stop-color="#0b1f3d"/>
        </linearGradient>
        <linearGradient id="back-rim" x1="0" y1="0" x2="0" y2="1">
          <stop offset="0.4" stop-color="#0455a3" stop-opacity="0"/>
          <stop offset="0.7" stop-color="#1a6fd0"/>
          <stop offset="1" stop-color="#0455a3"/>
        </linearGradient>
      </defs>
      <rect x="476" y="30" width="60" height="250" fill="url(#back-texture)"/>
      <rect width="200" height="309" fill="url(#back-corner)"/>
      <ellipse cx="393" cy="96" rx="395" ry="300" fill="url(#back-rim)"/>
      <ellipse cx="400" cy="90" rx="395" ry="300" fill="var(--brand-black)"/>
      <rect x="13" y="15" width="511" height="283" fill="none"
            stroke="#1e8ad6" stroke-width="1.2" stroke-dasharray="1.2 5"/>
    </svg>

    <div class="wordmark">Tandrel</div>

    <ul class="contact-list">
      <li class="contact-list__item">
        <svg class="contact-list__icon" viewBox="0 0 24 24" aria-hidden="true"><path d="M12 1a8 8 0 0 0-8 8c0 6 8 14 8 14s8-8 8-14a8 8 0 0 0-8-8zm0 11a3 3 0 1 1 0-6 3 3 0 0 1 0 6z"/></svg>
        48 Ferrow Lane, Kestrel Bay, Norvia
      </li>
      <li class="contact-list__item">
        <svg class="contact-list__icon" viewBox="0 0 24 24" aria-hidden="true"><path d="M2 8l10-6 10 6v13H2z"/><path d="M2 9l10 6 10-6" fill="none" stroke="#000" stroke-width="1.8"/></svg>
        mara.elden@tandrel.com
      </li>
      <li class="contact-list__item">
        <svg class="contact-list__icon" viewBox="0 0 24 24" aria-hidden="true"><path d="M6.6 10.8a15 15 0 0 0 6.6 6.6l2.2-2.2a1 1 0 0 1 1-.25 11.4 11.4 0 0 0 3.6.6 1 1 0 0 1 1 1V20a1 1 0 0 1-1 1A17 17 0 0 1 3 4a1 1 0 0 1 1-1h3.5a1 1 0 0 1 1 1c0 1.25.2 2.45.6 3.6a1 1 0 0 1-.25 1z"/></svg>
        +0047 318 552 904
      </li>
      <li class="contact-list__item">
        <svg class="contact-list__icon" viewBox="0 0 24 24" aria-hidden="true"><path d="M5 2l14 11-6.5 1 3.5 7.5-2.6 1.2-3.5-7.5L5 20z"/></svg>
        www.tandrelgroup.com
      </li>
    </ul>
  </section>

</main>
</body>
</html>
```